Zanquorra Business Card Design

Zanquorra is a small and new restaurant/ bar location in Hong Kong. The name "Djibouti" derives from an African country. There is no specific reason behind other than the fact, that the bar is somewhat inspired by African elements (only inspired but not purely based on African cuisine etc.).

The bar is somewhat a fusion of African, Mediterranean and Oriental (Old French Vietnam) elements.

However, it is very imperative to stress, that the overall look and feel of Zanquorra is a very high end cocktail lounge/ bar location. The bar is tucked away in a hidden alley, so people will have to know about it. The idea is to send the consumer off in an Escape or hidden remote location where they are at ease in a hip, stylish and trendy environment.

The card needs to feel high-end.

Final logo artwork has been attached and also pictures of the bar/ restaurant itself. The logo ie monkey head cannot be modified. However, the background color and the color of the type "ZANQUORRA" can be changed.

The following details need to fit onto the business card. Of course they can be arranged to your liking:

LOGO

Colin Vey
Partner

+852 97035164
xxx@zanquorra.com
www.zanquorra.com
7C, Brennick Road, Wan Chai, Hong Kong

```html
<!DOCTYPE html>
<html lang="en">
<head>
<meta charset="utf-8">
<title>Zanquorra Business Card</title>
<link href="https://fonts.googleapis.com/css2?family=Open+Sans:wght@400;600&display=swap" rel="stylesheet">
<style>
  :root {
    --stage: #3a3a3a;
    --card-dark: #1e1919;
    --card-mid: #3b2f2e;
    --card-warm: #4a3533;
    --card-floor: #2c2826;
    --accent-red: #6b2a35;
    --text-main: #f2efec;
    --text-soft: #d9d3cf;
    --rule: rgba(255,255,255,0.55);
  }
  * { margin: 0; padding: 0; box-sizing: border-box; }
  html, body {
    width: 1200px; height: 848px; overflow: hidden;
    background: var(--stage);
    font-family: "Open Sans", Arial, sans-serif;
  }
  .canvas {
    position: relative; width: 1200px; height: 848px;
    display: flex; justify-content: center; align-items: center; gap: 60px;
  }
  .card {
    position: relative; width: 400px; height: 600px; overflow: hidden;
    background: var(--card-dark);
    box-shadow: 0 10px 30px rgba(0,0,0,0.45);
  }
  .card__photo {
    position: absolute; inset: 0;
    background:
      radial-gradient(ellipse at 70% 12%, var(--accent-red) 0%, transparent 38%),
      linear-gradient(180deg, var(--card-mid) 0%, var(--card-warm) 45%, var(--card-dark) 72%, var(--card-floor) 100%);
    opacity: 0.9;
  }
  .brand {
    position: absolute; left: 0; right: 0;
    display: flex; flex-direction: column; align-items: center;
  }
  .brand__mark {
    border-radius: 50%; background: var(--text-main);
  }
  .brand__name {
    color: var(--text-main); font-weight: 600; letter-spacing: 3px;
  }
  .card--front .brand { top: 190px; gap: 22px; }
  .card--front .brand__mark { width: 150px; height: 150px; }
  .card--front .brand__name { font-size: 44px; }

  .card--back .brand { top: 34px; gap: 14px; }
  .card--back .brand__mark { width: 100px; height: 100px; }
  .card--back .brand__name { font-size: 30px; }

  .contact {
    position: absolute; left: 40px; right: 40px; top: 270px;
    color: var(--text-main);
  }
  .contact__name { font-size: 24px; font-weight: 600; line-height: 1.2; }
  .contact__role { font-size: 22px; color: var(--text-soft); margin-bottom: 12px; }
  .contact__address { font-size: 16px; line-height: 1.35; color: var(--text-soft); margin-bottom: 14px; }
  .contact__list { list-style: none; font-size: 16px; line-height: 1.6; }
  .contact__list li { display: flex; align-items: center; gap: 10px; }
  .contact__list svg { width: 15px; height: 15px; flex: none; }
  .rule {
    position: absolute; left: 40px; right: 40px; top: 510px;
    height: 1px; background: var(--rule);
  }
</style>
</head>
<body>
<main class="canvas">
  <section class="card card--front">
    <div class="card__photo" role="img" aria-label="Photograph of the bar's hidden alley entrance with brick wall, lattice screen, hanging lantern and wooden deck"></div>
    <div class="brand">
      <div class="brand__mark"></div>
      <div class="brand__name">ZANQUORRA</div>
    </div>
  </section>

  <section class="card card--back">
    <div class="card__photo" role="img" aria-label="Photograph of the bar's hidden alley entrance with brick wall, lattice screen, hanging lantern and wooden deck"></div>
    <div class="brand">
      <div class="brand__mark"></div>
      <div class="brand__name">ZANQUORRA</div>
    </div>
    <div class="contact">
      <p class="contact__name">Colin Vey</p>
      <p class="contact__role">Partner</p>
      <p class="contact__address">7C, Brennick Road, Wan Chai,<br>Hong Kong</p>
      <ul class="contact__list">
        <li>
          <svg viewBox="0 0 16 16" aria-hidden="true"><path fill="#f2efec" d="M3.5 1.5l2.5 3-1.5 1.5c.8 1.8 2.2 3.2 4 4l1.5-1.5 3 2.5-1.5 2.5C7 13 3 9 1.5 3z"/></svg>
          +852 97035164
        </li>
        <li>
          <svg viewBox="0 0 16 16" aria-hidden="true"><rect x="1.5" y="3.5" width="13" height="9" fill="none" stroke="#f2efec" stroke-width="1.2"/><path d="M1.5 3.5L8 9l6.5-5.5" fill="none" stroke="#f2efec" stroke-width="1.2"/></svg>
          xxx@zanquorra.com
        </li>
        <li>
          <svg viewBox="0 0 16 16" aria-hidden="true"><circle cx="8" cy="8" r="6.5" fill="none" stroke="#f2efec" stroke-width="1.1"/><ellipse cx="8" cy="8" rx="3" ry="6.5" fill="none" stroke="#f2efec" stroke-width="1.1"/><path d="M1.5 8h13" stroke="#f2efec" stroke-width="1.1"/></svg>
          www.zanquorra.com
        </li>
      </ul>
    </div>
    <div class="rule"></div>
  </section>
</main>
</body>
</html>
```